Kitchen manufaturer business card/logo design

I am a small kitchen manufacturing company that makes and installs all sorts of cabinetry.

The colours im looking to incorporate in the card are light/baby blue, white and black.

Incorporate 5 stars to show quality workmanship and product.

Looking for a modern classy design.
Updates

Hey guys, New idea. The logo should be made using HK in the most modern way possible as well as the full company name below it. Thanks.

Target Market(s)

Anyone with a home thats looking for a new cabinetry of any sort.

Industry/Entity Type

Business

Contact Information for Business Card

Harbor Kitchens
Ted Lowther
PH 0491 358 902
Email- harborkitchens@mailvane.example
ABN- 83 507 962 318
-Kitchens
-Vanities
-Laundries
-Media Units
-Studies
-Wardrobes
-3D Computer Designs

Requirements
Must have

• The front of the card must only have the company name.
The different types of cabinetry I do must be on the back of the card in point form but instead of using points use stars.
Nice to have
• Just think classy and quality

```html
<!DOCTYPE html>
<html lang="en">
<head>
<meta charset="utf-8">
<title>Harbor Kitchens – Business Cards</title>
<link rel="stylesheet" href="https://fonts.googleapis.com/css2?family=Arimo:wght@400;700&family=Pinyon+Script&display=swap">
<style>
  :root {
    --backdrop: #ece9e4;
    --baby-blue: #14a9e0;
    --baby-blue-light: #3cc0f0;
    --baby-blue-deep: #0b8ec4;
    --ink: #121212;
    --white: #ffffff;
    --star-grey: #9a9a9a;
  }
  * { box-sizing: border-box; margin: 0; padding: 0; }
  html, body { width: 1200px; height: 900px; overflow: hidden; }
  body {
    background: var(--backdrop);
    font-family: "Arimo", Arial, sans-serif;
    position: relative;
  }
  .card {
    position: absolute;
    width: 660px;
    height: 367px;
    overflow: hidden;
    box-shadow: 0 6px 18px rgba(0,0,0,.25);
  }
  .card-back { left: 40px; top: 60px; }
  .card-front {
    left: 500px; top: 470px;
    background: radial-gradient(ellipse at 50% 45%, var(--baby-blue-light) 0%, var(--baby-blue) 55%, var(--baby-blue-deep) 100%);
    display: flex; align-items: center; justify-content: center;
  }
  .card-back .backdrop { position: absolute; inset: 0; }
  .services {
    position: absolute; left: 34px; top: 22px;
    color: var(--white); font-size: 25px; line-height: 34px;
  }
  .services li { list-style: none; display: inline; margin-right: 6px; }
  .services .row { display: block; white-space: nowrap; }
  .star-bullet { width: 15px; height: 15px; fill: var(--star-grey); vertical-align: 1px; margin-right: 3px; }
  .owner-name {
    position: absolute; left: 78px; top: 128px;
    font-family: "Pinyon Script", cursive;
    font-size: 88px; font-weight: 400; color: var(--white); line-height: 1;
    white-space: nowrap;
  }
  .abn {
    position: absolute; left: 205px; top: 228px;
    font-size: 25px; color: var(--ink); white-space: nowrap;
  }
  .contact {
    position: absolute; left: 58px; right: 28px; bottom: 24px;
    display: flex; justify-content: space-between; align-items: flex-end;
    color: var(--white); font-size: 23px; white-space: nowrap;
  }
  .contact-item { display: flex; align-items: center; gap: 8px; flex-shrink: 0; }
  .contact-icon { width: 22px; height: 22px; fill: none; stroke: var(--white); stroke-width: 1.6; }
  .contact-icon.phone { fill: var(--white); stroke: none; }
  .company-name {
    color: var(--white); font-weight: 700; font-size: 58px;
    letter-spacing: 1px;
  }
</style>
</head>
<body>
  <svg width="0" height="0" style="position:absolute">
    <defs>
      <symbol id="star" viewBox="0 0 24 24">
        <path d="M12 1.5l3.1 6.9 7.4.7-5.6 5 1.7 7.4L12 17.7l-6.6 3.8 1.7-7.4-5.6-5 7.4-.7z"/>
      </symbol>
    </defs>
  </svg>

  <section class="card card-back" aria-label="Business card back">
    <svg class="backdrop" viewBox="0 0 660 367" width="660" height="367" aria-hidden="true">
      <defs>
        <linearGradient id="dark-band" x1="0" y1="0" x2="1" y2="0">
          <stop offset="0" stop-color="#6a6a6a"/>
          <stop offset=".55" stop-color="#2a2a2a"/>
          <stop offset="1" stop-color="#0a0a0a"/>
        </linearGradient>
        <linearGradient id="blue-band" x1="0" y1="0" x2="0" y2="1">
          <stop offset="0" stop-color="#0f9fd6"/>
          <stop offset=".2" stop-color="#1fb3ea"/>
          <stop offset=".85" stop-color="#1fb3ea"/>
          <stop offset="1" stop-color="#0f9fd6"/>
        </linearGradient>
      </defs>
      <rect width="660" height="367" fill="url(#dark-band)"/>
      <path d="M0 122 Q330 95 660 118 L660 268 Q330 285 0 292 Z" fill="url(#blue-band)" stroke="#bfe9fa" stroke-width="1.5"/>
    </svg>

    <ul class="services">
      <span class="row">
        <li><svg class="star-bullet"><use href="#star"/></svg>Kitchens</li>
        <li><svg class="star-bullet"><use href="#star"/></svg>Vanities</li>
        <li><svg class="star-bullet"><use href="#star"/></svg>Laundries</li>
        <li><svg class="star-bullet"><use href="#star"/></svg>Media Units</li>
      </span>
      <span class="row">
        <li><svg class="star-bullet"><use href="#star"/></svg>Studies</li>
        <li><svg class="star-bullet"><use href="#star"/></svg>Wardrobes</li>
        <li><svg class="star-bullet"><use href="#star"/></svg>3D Computer Designs</li>
      </span>
    </ul>

    <h1 class="owner-name">Ted Lowther</h1>
    <p class="abn">ABN- 83 507 962 318</p>

    <div class="contact">
      <span class="contact-item">
        <svg class="contact-icon phone" viewBox="0 0 24 24" aria-hidden="true"><path d="M6.6 10.8a15 15 0 006.6 6.6l2.2-2.2a1 1 0 011-.25 11.4 11.4 0 003.6.57 1 1 0 011 1V20a1 1 0 01-1 1A17 17 0 013 4a1 1 0 011-1h3.5a1 1 0 011 1c0 1.25.2 2.45.57 3.57a1 1 0 01-.25 1z"/></svg>
        0491 358 902
      </span>
      <span class="contact-item">
        <svg class="contact-icon" viewBox="0 0 24 24" aria-hidden="true"><rect x="2.5" y="5.5" width="19" height="13"/><path d="M2.5 5.5l9.5 8 9.5-8"/></svg>
        harborkitchens@mailvane.example
      </span>
    </div>
  </section>

  <section class="card card-front" aria-label="Business card front">
    <h2 class="company-name">Harbor Kitchens</h2>
  </section>
</body>
</html>
```